Sleek and Morden Business Card

Business Card Design for Business Name "Harbor Lantern Bureau (HLB)"
Offering Virtual Assistant (VA) services including Virtual Receptionist, Appointment and Diary Management. Taking and Answering calls for Sole Trader Businesses. Quotes, Invoices, Expense Reconciliation, Accounts Payable and Accounts Receivable.
Harbor Bureau offers clients the ease of a complete office without the physical need to having an office.
Target Market(s)
Target market are Sole Traders like Electricians, Plumbers, Painters etc.
Industry/Entity Type
Business
Colors
Designer to choose colors to be used in the design.
Look and feel
Each slider illustrates characteristics of the customer's brand and the style your logo design should communicate.

```html
<!DOCTYPE html>
<html lang="en">
<head>
<meta charset="utf-8">
<title>Harbor Lantern Bureau – Business Card</title>
<link href="https://fonts.googleapis.com/css2?family=Cormorant+Garamond:ital,wght@0,400;0,500;0,600;1,400;1,500;1,600&display=swap" rel="stylesheet">
<style>
  :root {
    --charcoal: #3a3a3a;
    --charcoal-deep: #2f2f2f;
    --lime: #a9c91c;
    --white: #ffffff;
    --frame-grey: #c9c9c9;
    --ink: #1a1a1a;
    --page: #ffffff;
    --script: "Cormorant Garamond", Georgia, serif;
  }
  * { box-sizing: border-box; margin: 0; padding: 0; }
  html, body {
    width: 930px; height: 1200px; overflow: hidden;
    background: var(--page);
  }
  .canvas { position: relative; width: 930px; height: 1200px; }

  .card {
    position: absolute;
    background: var(--charcoal);
    overflow: hidden;
    border: 1px solid #222;
  }
  .card-front { left: 40px; top: 14px; width: 850px; height: 520px; }
  .card-back  { left: 45px; top: 618px; width: 842px; height: 530px; }

  .corner-art { position: absolute; inset: 0; width: 100%; height: 100%; }

  /* Front */
  .front-frame {
    position: absolute; left: 44px; top: 47px; right: 45px; bottom: 44px;
    border: 2px solid var(--frame-grey);
    background: var(--charcoal-deep);
  }
  .brand-mark {
    position: absolute; left: 0; right: 0; top: 120px;
    text-align: center;
    font-family: var(--script); font-weight: 600; font-size: 118px;
    color: var(--lime); letter-spacing: 2px; line-height: 1;
  }
  .brand-name {
    position: absolute; left: 0; right: 0; top: 302px;
    text-align: center;
    font-family: var(--script); font-style: italic; font-weight: 500;
    font-size: 44px; color: var(--white);
  }

  /* Back */
  .back-panel {
    position: absolute; left: 44px; top: 45px; width: 753px; height: 441px;
    background: var(--white);
  }
  .monogram-area {
    position: absolute; left: 180px; top: 10px; width: 300px; height: 420px;
    border-radius: 50%;
    background: radial-gradient(ellipse at center, rgba(200,200,200,0.35), rgba(255,255,255,0) 70%);
  }
  .tagline {
    position: absolute; left: 0; right: 0; top: 48px;
    padding-left: 178px; text-align: center;
    font-family: var(--script); font-style: italic; font-weight: 500;
    font-size: 40px; color: var(--ink);
  }
  .service-band {
    position: absolute; left: 32px; top: 94px; right: 0; height: 250px;
    background: var(--charcoal);
  }
  .band-accent {
    position: absolute; left: 0; top: 0; width: 16px; height: 100%;
    background: var(--lime);
  }
  .illustration-slot {
    position: absolute; left: 16px; top: 3px; width: 232px; height: 244px;
    background: linear-gradient(160deg, #f3f3f3 0%, #e7c3a4 35%, #8a3a1f 65%, #4a4a4a 100%);
  }
  .band-copy {
    position: absolute; left: 263px; top: 10px; right: 16px;
    font-family: var(--script); font-style: italic; color: var(--white);
  }
  .band-title {
    font-size: 38px; font-weight: 500; color: var(--lime); line-height: 1.1;
    margin-bottom: 8px;
  }
  .band-services, .band-market {
    font-size: 20.5px; line-height: 22px; font-weight: 500;
  }
  .band-market { margin-top: 20px; }

  .contact {
    position: absolute; left: 16px; top: 346px;
    font-family: var(--script); color: var(--ink);
  }
  .contact-name { font-size: 29px; font-weight: 500; line-height: 1.1; }
  .contact-phone { font-size: 21px; margin-left: 12px; letter-spacing: 1px; line-height: 1.25; }
  .contact-email { font-size: 20px; margin-left: 12px; line-height: 1.25; }
  .closing {
    position: absolute; left: 380px; top: 352px; width: 360px; text-align: center;
    font-family: var(--script); font-style: italic; font-weight: 500;
    font-size: 36px; color: var(--ink);
  }
</style>
</head>
<body>
<main class="canvas">

  <section class="card card-front" aria-label="Card front">
    <svg class="corner-art" viewBox="0 0 850 520" preserveAspectRatio="none" aria-hidden="true">
      <polygon points="650,0 850,0 850,165" fill="#a9c91c"/>
      <polygon points="600,0 625,0 850,185 850,206" fill="#ffffff"/>
      <polygon points="0,330 0,520 215,520" fill="#a9c91c"/>
      <polygon points="0,300 0,322 240,520 218,520" fill="#ffffff"/>
    </svg>
    <div class="front-frame"></div>
    <div class="brand-mark">HLB</div>
    <div class="brand-name">Harbor Lantern Bureau</div>
  </section>

  <section class="card card-back" aria-label="Card back">
    <svg class="corner-art" viewBox="0 0 842 530" preserveAspectRatio="none" aria-hidden="true">
      <polygon points="680,0 842,0 842,120" fill="#a9c91c"/>
      <polygon points="640,0 662,0 842,135 842,155" fill="#ffffff"/>
      <polygon points="0,400 0,530 165,530" fill="#a9c91c"/>
      <polygon points="0,372 0,392 185,530 163,530" fill="#ffffff"/>
    </svg>
    <div class="back-panel">
      <div class="monogram-area" role="img" aria-label="Faint decorative script initial"></div>
      <div class="tagline">Virtual Assistance</div>
      <div class="service-band">
        <div class="band-accent"></div>
        <div class="illustration-slot" role="img" aria-label="Illustration of a receptionist with headset at a computer desk"></div>
        <div class="band-copy">
          <div class="band-title">Harbor Lantern Bureau</div>
          <p class="band-services">Services include: Virtual receptionist, Expense reconciliation, Accounts Payable and Accounts receivable, Quotes, Diary Management, Taking and Answering calls for sole trader business</p>
          <p class="band-market">Target market are Sole Traders like Electricians, Plumbers, Painters etc.</p>
        </div>
      </div>
      <div class="contact">
        <div class="contact-name">Mara Ellwood</div>
        <div class="contact-phone">0400 555 182</div>
        <div class="contact-email">mara@harborbureau.example</div>
      </div>
      <div class="closing">And so much more....</div>
    </div>
  </section>

</main>
</body>
</html>
```